need a Flyer for Plush Toy company

Need a Flyer for Plush Toy company ,

I upload a file for TEXT

Target Market(s)

Toys wholesalers , Supermarket

Industry/Entity Type

Toy Store

Colors
000000
ec1f27
c4c4c4

Requirements
Must have
• I have up loaded 3 files
• 1. Logo Registered Brand
• 2. customer's design in drawing
• 3. our ready samples based on Design
Nice to have
• happy kids in Nature ,
• happy kids in Ski ,
• different color Kids ,
• Multi culture concept

```html
<!DOCTYPE html>
<html lang="en">
<head>
<meta charset="utf-8">
<title>Momo Lane – Plush Toy Flyer</title>
<link href="https://fonts.googleapis.com/css2?family=Arimo:ital,wght@0,400;0,700;1,400&family=Kalam:wght@700&display=swap" rel="stylesheet">
<style>
  :root{
    --frame:#3b3b3b;
    --paper:#ffffff;
    --ink:#000000;
    --red:#ec1f27;
    --grey:#c4c4c4;
    --text-light:#ffffff;
  }
  *{box-sizing:border-box;margin:0;padding:0}
  html,body{width:800px;height:1200px;overflow:hidden;background:var(--frame)}
  .flyer{position:relative;width:800px;height:1200px;background:var(--frame);font-family:"Arimo",Arial,sans-serif}
  .card{position:absolute;left:24px;top:24px;width:752px;height:1152px;background:var(--paper);overflow:hidden}

  .header{position:absolute;left:0;top:0;width:752px;height:240px}
  .brand-illustration{position:absolute;left:20px;top:14px;width:200px;height:190px;
    background:radial-gradient(circle at 50% 45%,#f4f4f4,#d9d9d9);border-radius:12px}
  .brand-text{position:absolute;left:230px;top:22px;width:500px;text-align:center}
  .brand-name{font-size:50px;font-weight:700;color:var(--ink);letter-spacing:1px;line-height:1.05}
  .brand-line{color:var(--ink);line-height:1.3}
  .brand-line.lead{font-size:27px;margin-top:6px}
  .brand-line.sub{font-size:24px}
  .tagline{position:absolute;left:14px;top:196px;padding:2px 18px;border:3px solid var(--red);border-radius:22px;
    background:var(--paper);font-family:"Kalam",cursive;font-size:26px;color:var(--red);z-index:3}

  .swoosh{position:absolute;left:0;top:190px;width:752px;height:110px;z-index:2}

  .showcase{position:absolute;left:0;top:260px;width:752px;height:360px;background:var(--red)}
  .sofa-scene{position:absolute;left:100px;top:60px;width:560px;height:290px;border-radius:28px;
    background:linear-gradient(180deg,#f6f1e8 0%,#d6e7b4 45%,#a9c97a 100%)}

  .story{position:absolute;left:0;top:620px;width:752px;height:300px;background:var(--ink);
    color:var(--text-light);padding:26px 40px 0 40px;font-size:17px;line-height:1.45}
  .story p{margin-bottom:16px}
  .accent{color:var(--red);font-weight:700}

  .contact-zone{position:absolute;left:0;top:920px;width:752px;height:232px;background:var(--paper)}
  .samples-photo{position:absolute;left:14px;top:10px;width:300px;height:118px;border-radius:8px;
    background:linear-gradient(135deg,#f2d6e6,#cfe6f5 50%,#f5e7a8)}
  .contact-lines{position:absolute;left:380px;top:10px;font-size:14px;line-height:1.42;color:var(--ink)}
  .contact-lines .label{display:inline-block;width:58px}
  .footer-band{position:absolute;left:0;top:130px;width:752px;height:102px;background:var(--red);color:var(--text-light)}
  .address{position:absolute;left:22px;top:22px;font-size:26px;font-weight:700;line-height:1.2}
  .bank{position:absolute;left:380px;top:10px;font-size:14px;font-weight:700;line-height:1.38}
</style>
</head>
<body>
<div class="flyer">
  <div class="card">

    <header class="header">
      <div class="brand-illustration" role="img" aria-label="Illustration of children sailing a toy ship"></div>
      <div class="brand-text">
        <h1 class="brand-name">Momo Lane</h1>
        <p class="brand-line lead">Einzelunternehmen / Family Business</p>
        <p class="brand-line sub">International Trader for Toys</p>
        <p class="brand-line sub">Innovative Developer&nbsp; for Plush Toys</p>
      </div>
    </header>

    <svg class="swoosh" viewBox="0 0 752 110" preserveAspectRatio="none" aria-hidden="true">
      <path d="M0 60 C200 20 420 10 752 30 L752 110 L0 110 Z" fill="var(--red)"/>
      <path d="M0 62 C220 24 430 14 752 34 L752 44 C430 26 220 36 0 76 Z" fill="var(--ink)"/>
    </svg>
    <div class="tagline">Have you been there?</div>

    <section class="showcase">
      <div class="sofa-scene" role="img" aria-label="Illustration of plush toy characters sitting on a green sofa"></div>
    </section>

    <section class="story">
      <p>We live and work in Lindenfeld near to Cologne Germany. We speak German and English.</p>
      <p>The toys are made in China, we are small family business , but we are professional in Plush toys business , right now we have successfully&nbsp; launched Projects with a huge Japanese 100 Yen Chain Store.&nbsp; Here in Flyer we show a Sample project.</p>
      <p><span class="accent">100 Yen + 0.90 USD.</span> Our products can meet strictest Quality Control , but are with extremely Low Price to fit for&nbsp; Japanese Dollar Shop as well as his overseas Store around the world.</p>
      <p>&nbsp;Of course our products are fit for&nbsp; <span class="accent">Premium Store too.</span></p>
    </section>

    <section class="contact-zone">
      <div class="samples-photo" role="img" aria-label="Photo of finished plush toy samples"></div>
      <div class="contact-lines">
        <div>hello@momolane-toys.de</div>
        <div><span class="label">Fon</span>+49 (0) 2200- 555 0101</div>
        <div><span class="label">Fax</span>+49 (0) 2200- 555 0102</div>
        <div><span class="label">Mobil:</span>+49 (0) 150 5550 103</div>
        <div>Ust-IdNr./VAT No. DE000111222</div>
      </div>
      <div class="footer-band">
        <div class="address">Rosenpfad 8, 50999<br>Lindenfeld Germany</div>
        <div class="bank">
          <div>Bank Information :</div>
          <div>Kontoinhaber/Account Holder:</div>
          <div>Lin Hart</div>
          <div>IBAN:&nbsp; DE00 1234 5678 0000 1111 22</div>
          <div>BIC : DEMOBANKXXX</div>
        </div>
      </div>
    </section>

  </div>
</div>
</body>
</html>
```